Simple and clean poster/flyer design needed for public speaker!

SIMPLE AND CLEAN DESIGN NEEDED FOR POSTER/FLYER

I AM a public speaker based in London (www.tobiaskernwald.com)
and I would like to have a custom-made flyer/poster
(preferably in adobe CS4 template format) that I con customize (just changing the text) for my various speeches, topics and locations

I am looking for something very simple and clean.
NO extravagance or crowded poster, but a rather beautiful clean and eye-catching design that clearly informs people what i am talking about, where and when.

Go to my website www.tobiaskernwald.com
to see the colour scheme and style that I like
my poster should be like the website, similar colours, logo, clean, simple and clear.

Summary

(1) simple and clean design
(2) design that fits my brand (see website)
(3) clear and eye-catching to promote my speeches
(4) customizable for my various talks, by simply chancing the text (Please Adobe Photoshop CS4 template format)
(5)in A3, A4, A5, A6 sizes, so i can use it for both flyers and small posters

ADDITIONS

BIG BOLD HEADLINE TO GRAP ATTENTION, greatest prominence

sub headline to explain, smaller than the headline, but still prominent on the poster

just a few bullet points to list the benefits and answer the “whats in for me”-question
this is for people who are already interested and continue reading, medium prominence.

WHERE, WHEN, HOW MUCH-information, in the lower section of the poster, little text, but clearly visible

only one point of CONTACT on my poster “www.tobiaskernwald.com”, bit big and clear so that it is very prominent

little text, effectively used
LESS IS MORE
Updates

contact me regarding logo files and any questions you may have!

for the logo files go to

https://secure.dropvaultly.com/fs/v.aspx?v=41958b2d703c9ea1f6d2

click on the folder "logo pack" to see the files

eps
jpg
png
photoshop
TIF

thanks for your interest. hope to see great designs!
I am really looking forward to it
if you have any questions, please do not hesitate to ask

Kind Regards
Tobias
 

• Simple, clean design, text sparingly used.

• The mood should be light-hearted, calm, bright, simple and friendly, comic like

• a lot of white space, calling more attention to the content

• a light blue, dark blue, white and black colour scheme as seen on the homepage (www.tobiaskernwald.com) please use the exact same colours as seen on the homepage.

White being most predominant, 2 different blue used to highlight something, black for text on white background.

• One graphic would be cool, as long as it is blue. It could be waves-like graphic, or something like the white pattern in the background, in my case just in blue on white background > http://www.lumenquietharbor.org/., I do not mean exactly this graphic and not that crowded but a simple single graphic in blue as long as it fits the theme and feel of my poster

Top o f the poster

• (a )One short bold headline (TALK TITLE) with a sub-headline below it (hook)

• or (b) headline as question (…....?) and below sub-headline offering the solution (my talk ;-) of course)

• 3 benefits as on homepage, that I can adapt for each talk (bottom right of my start site “what are you looking for?” either blue on white, or as in the page white on blue...whatever looks better and fits the design). Not sure how that looks, and if to include it!

• the bottom of the poster will have “Where”-information “when”-information “ticket price” info

• contact at the very bottom...for more into or to purchase tickets (my website and email)

If you have any questions or need clarification please write me!

Requirements
Must have
• lot of white space
• less is more - simple design
• little text, little graphics- only used when necessary to greatest effect.
• light, friendly, modern feel
• blue-color scheme

```html
<!DOCTYPE html>
<html lang="en">
<head>
<meta charset="utf-8">
<title>Living Without Strain – Talk Poster</title>
<link rel="stylesheet" href="https://fonts.googleapis.com/css2?family=Archivo:wght@800;900&family=Open+Sans:wght@400;600;700;800&display=swap">
<style>
  :root {
    --stage: #a9abae;
    --paper: #ffffff;
    --navy: #18202f;
    --sky: #3aa8dc;
    --band-light: #6cb2d2;
    --band-bright: #0ea3e3;
    --rule: #858a90;
    --muted: #7c838d;
    --info: #8b8d90;
    --white: #ffffff;
  }
  * { margin: 0; padding: 0; box-sizing: border-box; }
  html, body { width: 1200px; height: 900px; overflow: hidden; }
  body {
    background: var(--stage);
    font-family: "Open Sans", Arial, sans-serif;
    position: relative;
  }
  .poster {
    position: absolute;
    left: 330px; top: 60px;
    width: 540px; height: 780px;
    background: var(--paper);
    box-shadow: 4px 6px 10px rgba(0,0,0,.35);
    overflow: hidden;
  }
  .top-bar {
    position: absolute; left: 0; top: 0; width: 100%; height: 11px;
    background: var(--band-light);
  }
  .hero-figure {
    position: absolute; left: 300px; top: 12px; width: 230px; height: 210px;
    background: radial-gradient(circle at 52% 45%, #1aa6e8 0%, #7cc8ee 18%, #d4ecf9 45%, rgba(255,255,255,0) 70%);
  }
  .headline {
    position: absolute; left: 30px; top: 22px;
    font-family: "Archivo", Arial, sans-serif;
    font-weight: 900;
    font-size: 62px; line-height: 62px;
    color: var(--navy);
    letter-spacing: -0.5px;
  }
  .subheadline {
    position: absolute; left: 32px; top: 222px;
    font-weight: 700; font-size: 21px;
    color: #4d5259;
    white-space: nowrap;
  }
  .subheadline .accent { color: var(--sky); }
  .divider {
    position: absolute; left: 30px; top: 282px; width: 482px; height: 4px;
    background: var(--rule);
  }
  .benefits { position: absolute; left: 32px; top: 308px; }
  .benefits-title {
    font-weight: 700; font-size: 23px; color: var(--muted);
    margin-bottom: 2px;
  }
  .benefits-list {
    list-style: none;
    font-weight: 700; font-size: 22px; line-height: 32px; color: var(--navy);
  }
  .accent-strip {
    position: absolute; left: 0; top: 462px; width: 340px; height: 16px;
    background: linear-gradient(90deg, rgba(108,178,210,.15), rgba(108,178,210,.7) 60%, rgba(108,178,210,.2));
  }
  .event-info {
    position: absolute; left: 30px; top: 492px;
    font-family: "Archivo", Arial, sans-serif;
    font-weight: 800; font-size: 27px; line-height: 32px;
    color: var(--info);
    text-transform: uppercase;
    white-space: nowrap;
  }
  .event-info .sep { color: var(--sky); }
  .contact-band {
    position: absolute; left: 0; top: 612px; width: 100%; height: 58px;
    background: var(--band-light);
  }
  .band-burst {
    position: absolute; left: 0; top: 612px; width: 170px; height: 90px;
    background: radial-gradient(ellipse at 20% 55%, rgba(255,255,255,.85) 0%, rgba(255,255,255,.3) 35%, rgba(255,255,255,0) 70%);
  }
  .contact-cta {
    position: absolute; left: 30px; top: 650px;
    font-weight: 800; font-size: 13px; color: var(--navy);
    text-transform: uppercase;
  }
  .contact-main {
    position: absolute; left: 0; top: 670px; width: 100%; height: 110px;
    background: var(--band-bright);
  }
  .contact-url {
    position: absolute; left: 28px; top: 678px;
    font-weight: 800; font-size: 34px; color: var(--white);
    white-space: nowrap;
  }
  .speaker-role {
    position: absolute; left: 30px; top: 722px;
    font-weight: 400; font-size: 15px; color: #9fdaf6;
    text-transform: uppercase; letter-spacing: .5px;
  }
  .contact-email {
    position: absolute; right: 24px; top: 722px;
    font-size: 11px; color: var(--white);
  }
</style>
</head>
<body>
  <main class="poster">
    <div class="top-bar"></div>
    <div class="hero-figure" role="img" aria-label="Blue glowing figure with raised arms amid a burst of light rays"></div>

    <h1 class="headline">Living<br>Without<br>Strain</h1>
    <p class="subheadline">Free <span class="accent">yourself</span> from <span class="accent">fear</span> and <span class="accent">worry</span>... <span class="accent">forever</span></p>

    <div class="divider"></div>

    <section class="benefits">
      <h2 class="benefits-title">What are you looking for?</h2>
      <ol class="benefits-list">
        <li>1. Improved self-esteem</li>
        <li>2. Inner peace and calm</li>
        <li>3. Greater purpose and meaning in life</li>
      </ol>
    </section>

    <div class="accent-strip" role="img" aria-label="Light blue slanted dash accent"></div>

    <p class="event-info">
      24.09.10 <span class="sep">//</span> 09:00-16:00 <span class="sep">//</span><br>
      Ashcombe Hall, London <span class="sep">//</span><br>
      Tickets £12 <span class="sep">//</span>
    </p>

    <div class="contact-band"></div>
    <div class="band-burst" role="img" aria-label="Soft white light burst"></div>
    <p class="contact-cta">For more info and to buy tickets, visit:</p>
    <div class="contact-main"></div>
    <p class="contact-url">www.tobiaskernwald.com</p>
    <p class="speaker-role">Spiritual Speaker</p>
    <p class="contact-email">contact@tobiaskernwald.com</p>
  </main>
</body>
</html>
```